Baseball Coaching Camp for 5-14year olds needs sales campaign

Local baseball coaching camp for children is in it's 22nd year running a 4-5 week series of summer camps. Each year we use email marketing beginning around December to sell our camps to the parents to sign up their children for one or more weeks. All information about the camps can be seen on our website at https://quernhill.net/. In the past we have had success by changing the look of the emails each month and offering a decreasing discount as the camps get closer.

Our target market is the parents of children ages 5-14years old who like and play baseball and are interested in improving their skills in a fun environment during the Summer months.

We would like to improve the sales by developing new creative and imaginative emails for this season. We need 6 to 8 quality ads that can somehow relate to each other , these ads will be sent via our mailing list as well as used on social media. One of the owners thought it would be nice to use the "lantern harbor" theme though we are open to all ideas.
We have given you access to a dropbox link with examples of past campaigns along with artwork and images here
https://www.filecrate.example/sh/q7tmwpz2kdrlvha/BBKfe-moWenaXr7QuLP815cXo?dl=0

```html
<!DOCTYPE html>
<html lang="en">
<head>
<meta charset="utf-8">
<title>Quernhill Baseball Camp 2021</title>
<link rel="stylesheet" href="https://fonts.googleapis.com/css2?family=Anton&family=Poppins:wght@400;500;600;700&family=Roboto+Condensed:wght@500;700&display=swap">
<style>
  :root {
    --page: #f6f7f9;
    --edge: #cfe2ee;
    --hero-black: #000000;
    --flame-red: #ff3d12;
    --sky-blue: #17b1ff;
    --sun-yellow: #ffd45c;
    --gold: #f5c518;
    --field-green: #007a33;
    --navy: #001f6e;
    --phone-yellow: #ffd200;
    --white: #ffffff;
    --ink: #111111;
    --silver: #c9ccd1;
    --social-blue: #0c43b3;
    --social-pink: #c8349f;
  }
  * { box-sizing: border-box; margin: 0; padding: 0; }
  html, body { width: 1200px; height: 2835px; overflow: hidden; }
  body { background: var(--page); position: relative; font-family: "Poppins", sans-serif; }
  .edge-strip { position: absolute; left: 0; top: 0; width: 13px; height: 2835px; background: var(--edge); }

  .hero { position: absolute; left: 58px; top: 47px; width: 1098px; height: 1374px; background: var(--hero-black); overflow: hidden; }
  .hero-art { position: absolute; left: 440px; top: 0; width: 658px; height: 1374px;
    background: linear-gradient(160deg, #0a0a0a 0%, #1d4f8f 30%, #7a2a1c 60%, #c8472a 75%, #0a0a0a 100%); }
  .brand { position: absolute; left: 24px; top: 196px; height: 90px; display: flex; align-items: center; gap: 18px; }
  .brand-dot { width: 48px; height: 48px; border-radius: 50%; background: var(--silver); }
  .brand-name { font-family: "Anton", sans-serif; font-size: 72px; line-height: 90px; color: var(--silver); letter-spacing: 2px; }
  .camp-title { position: absolute; left: 42px; top: 354px; font-family: "Anton", sans-serif; font-weight: 400; font-style: oblique 10deg; color: var(--flame-red); font-size: 76px; line-height: 110px; text-transform: uppercase; }
  .camp-year { position: absolute; left: 24px; top: 694px; font-family: "Anton", sans-serif; font-style: oblique 10deg; color: var(--sky-blue); font-size: 194px; line-height: 200px; }
  .tagline { position: absolute; left: 24px; top: 931px; font-family: "Roboto Condensed", sans-serif; font-weight: 500; font-size: 44px; line-height: 60px; color: var(--white); text-transform: uppercase; }
  .tagline .accent { color: var(--sky-blue); display: block; }
  .register-btn { position: absolute; left: 24px; top: 1085px; width: 452px; height: 90px; background: var(--sun-yellow); display: flex; align-items: center; justify-content: center; font-family: "Anton", sans-serif; font-style: oblique 10deg; font-size: 40px; color: var(--ink); letter-spacing: 1px; }

  .offer-badge { position: absolute; left: 714px; top: 66px; width: 356px; height: 356px; border-radius: 50%; background: var(--sun-yellow); text-align: center; color: var(--ink); }
  .offer-kicker { margin-top: 66px; font-weight: 700; font-size: 34px; line-height: 40px; }
  .offer-amount { font-family: "Anton", sans-serif; color: var(--flame-red); font-size: 116px; line-height: 118px; }
  .offer-amount small { font-size: 58px; vertical-align: 34px; }
  .offer-label { font-weight: 500; font-size: 28px; line-height: 34px; }
  .offer-code { font-weight: 700; color: var(--flame-red); font-size: 36px; line-height: 40px; letter-spacing: 1px; }

  .schedule { position: absolute; left: 58px; top: 1421px; width: 549px; height: 699px; background: var(--field-green); padding: 34px 0 0 37px; color: var(--white); }
  .schedule-title { color: var(--gold); font-weight: 700; font-size: 34px; line-height: 50px; margin-bottom: 20px; }
  .session { margin-bottom: 58px; }
  .session:first-of-type { margin-bottom: 40px; }
  .session-week { font-weight: 600; font-size: 28px; line-height: 44px; }
  .session-detail { font-weight: 400; font-size: 28px; line-height: 44px; }
  .ages { position: absolute; left: 58px; top: 2120px; width: 549px; height: 141px; background: var(--hero-black); color: var(--white); font-weight: 600; font-size: 44px; display: flex; align-items: center; padding-left: 116px; }
  .batter-photo { position: absolute; left: 607px; top: 1421px; width: 549px; height: 840px;
    background: linear-gradient(180deg, #3f6b3a 0%, #5b8a4f 22%, #6f9b5c 28%, #b49578 40%, #c7a888 70%, #b89779 100%); }

  .contact { position: absolute; left: 58px; top: 2266px; width: 1098px; height: 318px; background: var(--navy); text-align: center; }
  .contact-lead { margin-top: 41px; color: var(--white); font-weight: 500; font-size: 45px; letter-spacing: 1px; line-height: 60px; }
  .contact-phone { margin-top: 24px; color: var(--phone-yellow); font-weight: 700; font-size: 104px; line-height: 140px; letter-spacing: 3px; }

  .social { position: absolute; top: 2683px; left: 0; width: 1200px; display: flex; justify-content: center; gap: 18px; }
  .social-link { width: 92px; height: 92px; border-radius: 50%; display: block; }
  .social-link.one { background: var(--social-blue); }
  .social-link.two { background: var(--social-pink); }
</style>
</head>
<body>
  <div class="edge-strip"></div>

  <section class="hero">
    <div class="hero-art" role="img" aria-label="Baseball wreathed in swirling red and blue smoke on black"></div>
    <div class="brand"><span class="brand-dot"></span><span class="brand-name">QUERNHILL</span></div>
    <h1 class="camp-title">Quernhill<br>Baseball<br>Camp</h1>
    <div class="camp-year">2021</div>
    <p class="tagline">Put your child on the <span class="accent">field this summer</span></p>
    <a class="register-btn">REGISTER NOW</a>
    <div class="offer-badge">
      <div class="offer-kicker">SAVE MONEY</div>
      <div class="offer-amount">$25<small> OFF</small></div>
      <div class="offer-label">PROMOCODE</div>
      <div class="offer-code">QRN2021</div>
    </div>
  </section>

  <section class="schedule">
    <h2 class="schedule-title">SCHEDULE</h2>
    <div class="session"><div class="session-week">Week 1</div><div class="session-detail">Dec 05-12, Town Park, Alderby</div></div>
    <div class="session"><div class="session-week">Week 1</div><div class="session-detail">Dec 05-12, Town Park, Alderby</div></div>
    <div class="session"><div class="session-week">Week 1</div><div class="session-detail">Dec 05-12, Town Park, Alderby</div></div>
    <div class="session"><div class="session-week">Week 1</div><div class="session-detail">Dec 05-12, Town Park, Alderby</div></div>
  </section>
  <div class="ages">Ages 5 - 14</div>
  <div class="batter-photo" role="img" aria-label="Young batter in a yellow jersey swinging at home plate on a youth baseball field"></div>

  <section class="contact">
    <p class="contact-lead">For more queries please call us.</p>
    <p class="contact-phone">(555) 014-2290</p>
  </section>

  <nav class="social">
    <a class="social-link one" aria-label="Social page"></a>
    <a class="social-link two" aria-label="Photo feed"></a>
  </nav>
</body>
</html>
```